Stationery Design Project

We are a packaging machinery manufacturer that mainly serve the food industry.
We now require a full set of stationary including name card, envelop, letter paper, and etc. to match our company image. The logo has been awarded in a previous contest which is attached here.
Updates
Project Deadline Extended
Reason: We have extended the deadline. We have adjusted the deadline before launch to avoid confusion but it turns out the new date wasn't implemented by the system. All designers please feel free to submit your design. Thank you!
Target Market(s)
B2B customer, including decision maker in food factories, chemical factories, etc.
Industry/Entity Type
Industry
Colors
Designer to choose colors to be used in the design.
Look and feel
Each slider illustrates characteristics of the customer's brand and the style your logo design should communicate.

```html
<!DOCTYPE html>
<html lang="en">
<head>
<meta charset="utf-8">
<title>Vorell Envelope</title>
<link rel="stylesheet" href="https://fonts.googleapis.com/css2?family=EB+Garamond:wght@400;600&display=swap">
<style>
  :root {
    --backdrop: #76797d;
    --paper: #ffffff;
    --paper-edge: #c9c9c9;
    --ink: #2a2a2a;
    --brand-green: #0d6b3b;
    --window-edge: #b9b9b9;
    --window-light: #f6f6f6;
    --window-mid: #e3e3e3;
  }
  html, body {
    margin: 0;
    padding: 0;
    width: 1200px;
    height: 1000px;
    overflow: hidden;
    background: var(--backdrop);
  }
  .canvas {
    position: relative;
    width: 1200px;
    height: 1000px;
  }
  .envelope {
    position: absolute;
    left: 48px;
    top: 222px;
    width: 1082px;
    height: 470px;
    background: var(--paper);
    border: 1px solid var(--paper-edge);
    box-sizing: border-box;
  }
  .brand {
    position: absolute;
    left: 34px;
    top: 46px;
    display: flex;
    align-items: center;
    gap: 7px;
    color: var(--brand-green);
    font-family: "EB Garamond", Georgia, serif;
    font-weight: 600;
    font-size: 30px;
    letter-spacing: 1px;
    line-height: 1;
  }
  .brand-square {
    width: 22px;
    height: 22px;
    background: var(--brand-green);
  }
  .return-address {
    position: absolute;
    left: 194px;
    top: 45px;
    margin: 0;
    font-family: "EB Garamond", Georgia, serif;
    font-style: normal;
    font-size: 19px;
    line-height: 24px;
    color: var(--ink);
  }
  .address-window {
    position: absolute;
    left: 102px;
    top: 284px;
    width: 510px;
    height: 125px;
    border: 1px solid var(--window-edge);
    border-radius: 20px;
    box-sizing: border-box;
    background: linear-gradient(160deg, var(--window-mid) 0%, var(--window-light) 35%, var(--window-mid) 60%, var(--window-light) 100%);
  }
</style>
</head>
<body>
  <div class="canvas">
    <div class="envelope">
      <div class="brand">
        <span class="brand-square"></span>
        <span class="brand-name">VORELL</span>
      </div>
      <address class="return-address">
        Marcus Hadley<br>
        2086 Pinecrest Rd<br>
        Fort Collins, CO&nbsp;&nbsp;80521
      </address>
      <div class="address-window"></div>
    </div>
  </div>
</body>
</html>
```